Spa Business Card Design Project

Hello! We are a boutique spa for men and women that is rebranding. I would like a memorable new business card that showcases our beautiful new logo and our unique business. I would like it to be classic/timeless and eclectic/artistic at the  same time.
I am a fan of negative space as you can tell from the logo. I am also open to any creative ideas.
Multi sided design. Two sided design is acceptable as an option, too. "Flaps/folds/whatever the design term is" are optional- whether full vertical or horizontal, half flap, full flap etc
On either side next to the golden snail I would potentially like to see "slow down. Enjoy Life."  Possibly on one statment on top of each other, crowned with the snail. Or the statment following the snail on one line... I am open for a creative suprise, too.
The back I would like room for the standard Information
"3817 Birch Lane
Alderbrook, New York 12853
(518) 462 3085
info@thecorvella spa.com
The snail is to be done in gold ink.
Can I also Have an option for cards that are individualized for staff members, too?

Updates
Project Deadline Extended
Reason: I apologize for the deadline extension. My day was more involved than anticipated in other matters. Hope to have this closed by next Tuesday.
Thank you

Target Market(s)
Men and women with expendable income between the ages of 30-55
Industry/Entity Type
Boutique
Requirements
Must have
- only black and gold ink.

Nice to have
- One of a kind.
Showcase the snail :-)
make you smile :-)
Fun, but professional.
Should not have
- Lots of color.
Too feminine.
Too busy.

```html
<!DOCTYPE html>
<html lang="en">
<head>
<meta charset="utf-8">
<title>The Corvella Spa – Business Cards</title>
<link rel="stylesheet" href="https://fonts.googleapis.com/css2?family=Cinzel:wght@400&family=Questrial&display=swap">
<style>
  :root {
    --gold: #d0ad6b;
    --gold-soft: #dcbd83;
    --ink: #111111;
    --paper: #ffffff;
    --stage: #8a6442;
    --label: #1a120b;
    --serif: "Cinzel", "Times New Roman", serif;
    --sans: "Questrial", Arial, sans-serif;
  }
  * { margin: 0; padding: 0; box-sizing: border-box; }
  html, body { width: 1200px; height: 788px; overflow: hidden; }
  body { position: relative; background: var(--stage); font-family: var(--sans); }

  .view-label {
    position: absolute; width: 526px; text-align: center;
    font-family: var(--sans); font-size: 20px; color: var(--label);
  }
  .card {
    position: absolute; width: 526px; height: 300px;
    border-radius: 18px; overflow: hidden; background: var(--paper);
    box-shadow: 0 6px 14px rgba(0,0,0,.35);
  }
  .card--dark { background: var(--ink); }

  .brand {
    position: absolute; font-family: var(--serif); font-weight: 400;
    line-height: .95; text-align: center; color: var(--ink);
  }
  .brand-dot {
    display: inline-block; border-radius: 50%; background: var(--gold);
    vertical-align: top;
  }
  .tagline { position: absolute; font-family: var(--sans); color: var(--ink); text-align: center; white-space: nowrap; }
  .web { position: absolute; font-family: var(--sans); letter-spacing: .28em; text-align: center; white-space: nowrap; }

  /* Front */
  .front-shape { position: absolute; inset: 0; }
  .motto {
    position: absolute; left: 58px; top: 20px; font-family: var(--serif);
    font-size: 13px; color: var(--gold); letter-spacing: .08em;
  }
  .front .brand { left: 20px; top: 70px; width: 300px; font-size: 40px; }
  .front .brand-dot { width: 10px; height: 10px; margin-right: 4px; margin-top: 6px; }
  .front .tagline { left: 20px; top: 180px; width: 300px; font-size: 12.5px; }
  .address { position: absolute; left: 20px; top: 242px; width: 266px; text-align: center; font-size: 13px; line-height: 17px; color: #333; }
  .staff { position: absolute; right: 18px; top: 106px; text-align: right; color: var(--ink); }
  .staff-name { font-family: var(--serif); font-size: 21px; letter-spacing: .02em; }
  .staff-role { font-family: var(--serif); font-size: 13px; letter-spacing: .05em; margin-top: 4px; }
  .contact { position: absolute; right: 18px; top: 214px; text-align: right; font-size: 13px; line-height: 20px; color: var(--ink); }

  /* Back 1 & 3 */
  .back-logo .brand { left: 0; top: 48px; width: 526px; font-size: 62px; }
  .back-logo .brand-dot { width: 14px; height: 14px; margin-right: 6px; margin-top: 8px; }
  .back-logo .tagline { left: 0; top: 222px; width: 526px; font-size: 19px; }
  .back-logo .web { left: 0; top: 271px; width: 526px; font-size: 12.5px; color: #222; }
  .card--dark .brand { top: 32px; }
  .card--dark .tagline { top: 206px; }
  .card--dark .brand, .card--dark .tagline, .card--dark .web { color: var(--paper); }

  /* Back 2 */
  .snail-art {
    position: absolute; left: 36px; top: 6px; width: 442px; height: 294px;
    background: var(--gold); border-radius: 52% 46% 0 0 / 62% 58% 0 0;
  }
  .mini .brand { left: 14px; top: 16px; width: 140px; font-size: 19px; }
  .mini .brand-dot { width: 5px; height: 5px; margin-right: 2px; margin-top: 3px; }
  .mini .tagline { left: 14px; top: 72px; width: 140px; font-size: 7.5px; }
  .mini .web { left: 0; top: 280px; width: 526px; font-size: 12px; color: var(--paper); }
</style>
</head>
<body>

  <div class="view-label" style="left:54px; top:34px;">Front</div>
  <div class="view-label" style="left:622px; top:34px;">Back - 1</div>
  <div class="view-label" style="left:54px; top:404px;">Back - 2</div>
  <div class="view-label" style="left:622px; top:404px;">Back - 3</div>

  <section class="card front" style="left:54px; top:74px;">
    <svg class="front-shape" width="526" height="300" viewBox="0 0 526 300" aria-hidden="true">
      <path d="M300 0 C345 60 300 150 292 200 C286 245 292 280 300 300 L526 300 L526 0 Z" fill="var(--gold)"/>
      <path d="M286 0 L298 0 C338 60 304 130 296 180 C300 120 320 60 286 0 Z" fill="var(--ink)"/>
    </svg>
    <p class="motto">slow down &amp; Enjoy Life.</p>
    <h1 class="brand"><span class="brand-dot"></span>The<br>Corvella<br>Spa</h1>
    <p class="tagline">a boutique spa for Men &amp; Women</p>
    <p class="address">3817 Birch Lane<br>Alderbrook, New York 12853</p>
    <div class="staff">
      <p class="staff-name">Your Name</p>
      <p class="staff-role">Designation</p>
    </div>
    <p class="contact">phone : (518) 462 3085<br>web : www.thecorvellaspa.com<br>email : info@thecorvellaspa.com</p>
  </section>

  <section class="card back-logo" style="left:622px; top:74px;">
    <h2 class="brand"><span class="brand-dot"></span>The<br>Corvella<br>Spa</h2>
    <p class="tagline">a boutique spa for Men &amp; Women</p>
    <p class="web">www.thecorvellaspa.com</p>
  </section>

  <section class="card mini" style="left:54px; top:445px;">
    <div class="snail-art" role="img" aria-label="Large gold snail illustration with spiral shell"></div>
    <h2 class="brand"><span class="brand-dot"></span>The<br>Corvella<br>Spa</h2>
    <p class="tagline">a boutique spa for Men &amp; Women</p>
    <p class="web">www.thecorvellaspa.com</p>
  </section>

  <section class="card card--dark back-logo" style="left:622px; top:445px;">
    <h2 class="brand"><span class="brand-dot"></span>The<br>Corvella<br>Spa</h2>
    <p class="tagline">a boutique spa for Men &amp; Women</p>
    <p class="web">www.thecorvellaspa.com</p>
  </section>

</body>
</html>
```